Scrap Metal Recycling

We are looking for a simple yet bold business card. We already have the logo, please see attached. Color scheme of blue, black and white or just blue and white.

```html
<!DOCTYPE html>
<html lang="en">
<head>
<meta charset="utf-8">
<title>Ridgeway Alloys Inc. — Business Card</title>
<link rel="stylesheet" href="https://fonts.googleapis.com/css2?family=Inter:wght@400;600&family=Open+Sans:wght@600&display=swap">
<style>
  :root {
    --backdrop: #2a2a2b;
    --card: #222224;
    --card-edge: #2c2c2e;
    --white: #f1f1f1;
    --muted: #d6d6d6;
    --blue: #1a8bb0;
  }
  * { margin: 0; padding: 0; box-sizing: border-box; }
  html, body {
    width: 1200px; height: 1138px; overflow: hidden;
    background: var(--backdrop);
  }
  .canvas { position: relative; width: 1200px; height: 1138px; }
  .card {
    position: absolute; width: 622px; height: 375px; border-radius: 16px;
    background: linear-gradient(160deg, var(--card) 0%, var(--card-edge) 100%);
    color: var(--white); font-family: "Inter", sans-serif; text-align: center;
  }
  .card--front { left: 274px; top: 186px; display: flex; align-items: center; justify-content: center; gap: 16px; }
  .card--back  { left: 276px; top: 608px; }

  .front-mark { width: 22px; height: 22px; background: var(--white); }
  .front-name { font-weight: 600; font-size: 40px; letter-spacing: 1px; color: var(--white); }

  .company { position: absolute; left: 0; right: 0; top: 76px; }
  .company__name { font-weight: 600; font-size: 36px; letter-spacing: 0.5px; color: var(--white); line-height: 1; }
  .company__tagline {
    margin-top: 10px; font-family: "Open Sans", sans-serif; font-weight: 600;
    font-size: 19px; letter-spacing: 6.6px; color: var(--blue);
  }

  .person { position: absolute; left: 0; right: 0; top: 226px; }
  .person__name { font-weight: 600; font-size: 23px; color: var(--blue); letter-spacing: -0.3px; }
  .person__role { margin-top: 2px; font-size: 15px; color: var(--muted); }

  .contact { position: absolute; left: 0; right: 0; top: 292px; font-size: 14.5px; color: var(--muted); line-height: 23px; }
  .contact__sep { margin: 0 8px; }
</style>
</head>
<body>
<main class="canvas">
  <section class="card card--front" aria-label="Card front">
    <span class="front-mark" aria-hidden="true"></span>
    <span class="front-name">Ridgeway Alloys Inc.</span>
  </section>

  <section class="card card--back" aria-label="Card back">
    <div class="company">
      <p class="company__name">RIDGEWAY ALLOYS INC.</p>
      <p class="company__tagline">SCRAP METAL RECYCLING</p>
    </div>
    <div class="person">
      <p class="person__name">DANIEL R. MARSH</p>
      <p class="person__role">Managing Director</p>
    </div>
    <div class="contact">
      <p>P: 000-555-0142<span class="contact__sep">|</span>E: daniel@ridgewayalloys.com<span class="contact__sep">|</span>W: www.ridgewayalloys.com</p>
      <p>A: 88 Foundry Lane, Millbrook, Any State, US 204519</p>
    </div>
  </section>
</main>
</body>
</html>
```